Independence Day Graphics for Sale

I want to create 10 social media graphics (new Pictora size 4:5 (1080 x 1350 pixels) focusing on our July 4th Sale Graphics, using any of the pics attached. Use the attached pics, NO RANDOM STOCK PHOTOGRAPHY. For the color scheme of the graphics, they should all be complementary to the product colors in the photos.
You can add any of the photos attached but none are required. You can do some of the graphics in all text. I mainly need BOLD text that says one of the headlines (10 total) SEE ATTACHED WORD DOCUMENT for the headlines to use.

Target Market(s)

women looking to lose weight

Requirements
Must have
• pics attached and text attached

```html
<!DOCTYPE html>
<html lang="en">
<head>
<meta charset="utf-8">
<title>July 4th Sale Graphics</title>
<link href="https://fonts.googleapis.com/css2?family=Bebas+Neue&display=swap" rel="stylesheet">
<style>
  :root {
    --pink: #c75a9b;
    --plum: #a2457f;
    --teal: #4f8f7e;
    --forest: #244a3e;
    --blue: #2b5bbd;
    --red: #e8302f;
    --indigo: #3f2d73;
    --white: #ffffff;
    --page: #ffffff;
    --studio-light: #fafafa;
    --studio-dark: #e3e3e3;
  }
  * { box-sizing: border-box; margin: 0; padding: 0; }
  html, body { width: 1200px; height: 594px; overflow: hidden; background: var(--page); }
  body { position: relative; font-family: "Bebas Neue", "Oswald", sans-serif; }

  .sale-post {
    position: absolute;
    width: 216px;
    height: 270px;
    overflow: hidden;
    background: linear-gradient(180deg, var(--white) 0%, var(--white) 38%, var(--studio-light) 55%, var(--studio-dark) 100%);
    box-shadow: 0 0 0 1px #eeeeee;
  }
  .col-1 { left: 40px; } .col-2 { left: 266px; } .col-3 { left: 492px; } .col-4 { left: 718px; } .col-5 { left: 943px; }
  .row-1 { top: 22px; } .row-2 { top: 302px; }

  .headline {
    position: absolute;
    left: 0; right: 0; top: 16px; height: 52px;
    display: flex; flex-direction: column; align-items: center; justify-content: center;
    text-align: center; line-height: 0.88; letter-spacing: -0.3px;
  }
  .headline.two-line { font-size: 25px; }
  .headline.one-line { font-size: 40px; }
  .headline.split { flex-direction: row; gap: 6px; }
  .headline .big { font-size: 44px; line-height: 0.85; }
  .headline .stack { font-size: 22px; line-height: 0.88; text-align: left; }

  .offer-box {
    position: absolute;
    left: 33px; width: 150px; top: 70px; height: 75px;
    color: var(--white);
    display: flex; flex-direction: column; align-items: center; justify-content: center;
    line-height: 0.86; z-index: 2;
  }
  .offer-box.compact { top: 74px; height: 54px; }
  .offer-box .amount { font-size: 45px; letter-spacing: 0.5px; }
  .offer-box .detail { font-size: 26px; margin-top: 1px; }
  .offer-box .detail.spaced { font-size: 23px; letter-spacing: 9px; margin-right: -9px; }
  .offer-box .detail.small { font-size: 17px; margin-top: 4px; }
  .offer-box .detail.medium { font-size: 21px; margin-top: 3px; }

  .product-photo {
    position: absolute;
    left: 10px; right: 10px; top: 150px; bottom: 12px;
    border-radius: 4px;
    background: linear-gradient(180deg, #f2f2f2 0%, #f7f7f7 40%, #e9e9ea 100%);
  }

  .bg-plum { background: var(--plum); }
  .bg-forest { background: var(--forest); }
  .bg-blue { background: var(--blue); }
  .bg-indigo { background: var(--indigo); }
  .bg-red { background: var(--red); }
  .c-pink { color: var(--pink); }
  .c-teal { color: var(--teal); }
  .c-blue { color: var(--blue); }
  .c-red { color: var(--red); }
</style>
</head>
<body>

  <section class="sale-post col-1 row-1">
    <h2 class="headline two-line c-pink"><span>The lowest prices</span><span>we've ever offered!</span></h2>
    <div class="offer-box compact bg-plum"><span class="amount">25% OFF</span></div>
    <div class="product-photo" role="img" aria-label="Four white supplement bottles standing in a row on a light studio background"></div>
  </section>

  <section class="sale-post col-2 row-1">
    <h2 class="headline one-line c-teal"><span>One-time only:</span></h2>
    <div class="offer-box bg-forest"><span class="amount">25% OFF</span><span class="detail">of everything!</span></div>
    <div class="product-photo" role="img" aria-label="Four white supplement bottles spaced evenly on a light studio background"></div>
  </section>

  <section class="sale-post col-3 row-1">
    <h2 class="headline two-line c-blue"><span>Biggest <span class="c-red">4th of July</span></span><span>sale ever!</span></h2>
    <div class="offer-box bg-blue"><span class="amount">25% OFF</span><span class="detail spaced">sitewide</span></div>
    <div class="product-photo" role="img" aria-label="Four white supplement bottles grouped together on a light studio background"></div>
  </section>

  <section class="sale-post col-4 row-1">
    <h2 class="headline two-line c-blue"><span>Mega summer</span><span>blowout!</span></h2>
    <div class="offer-box bg-indigo"><span class="amount">25% OFF</span><span class="detail">of everything!</span></div>
    <div class="product-photo" role="img" aria-label="Four white supplement bottles spaced evenly on a light studio background"></div>
  </section>

  <section class="sale-post col-5 row-1">
    <h2 class="headline two-line c-blue"><span>Our biggest</span><span>discount ever!</span></h2>
    <div class="offer-box bg-red"><span class="amount">25% OFF</span><span class="detail">of everything!</span></div>
    <div class="product-photo" role="img" aria-label="Four white supplement bottles grouped together on a light studio background"></div>
  </section>

  <section class="sale-post col-1 row-2">
    <h2 class="headline split c-blue"><span class="big">July 4th</span><span class="stack">Mega<br>sale!</span></h2>
    <div class="offer-box bg-red"><span class="amount">25% OFF</span><span class="detail">of everything!</span></div>
    <div class="product-photo" role="img" aria-label="Four white supplement bottles grouped together on a light studio background"></div>
  </section>

  <section class="sale-post col-2 row-2">
    <h2 class="headline two-line c-blue"><span>Historic</span><span>4th of July sale!</span></h2>
    <div class="offer-box bg-indigo"><span class="amount">25% OFF</span><span class="detail">of everything!</span></div>
    <div class="product-photo" role="img" aria-label="Four white supplement bottles spaced evenly on a light studio background"></div>
  </section>

  <section class="sale-post col-3 row-2">
    <h2 class="headline one-line c-pink"><span>Last chance</span></h2>
    <div class="offer-box bg-plum"><span class="amount">25% OFF</span><span class="detail small">Time is running out!</span></div>
    <div class="product-photo" role="img" aria-label="Four white supplement bottles grouped together on a light studio background"></div>
  </section>

  <section class="sale-post col-4 row-2">
    <h2 class="headline one-line c-red"><span>Don't wait!</span></h2>
    <div class="offer-box bg-blue"><span class="amount">25% OFF</span><span class="detail spaced">Ends soon</span></div>
    <div class="product-photo" role="img" aria-label="Four white supplement bottles spaced evenly on a light studio background"></div>
  </section>

  <section class="sale-post col-5 row-2">
    <h2 class="headline split c-teal"><span class="big">25% OFF</span><span class="stack">Stock-up<br>event:</span></h2>
    <div class="offer-box bg-forest"><span class="amount">25% OFF</span><span class="detail medium">All supplements</span></div>
    <div class="product-photo" role="img" aria-label="Four white supplement bottles grouped together on a light studio background"></div>
  </section>

</body>
</html>
```